■成果物
新聞広告(カラー突き出し)天地9.8cm×左右6.3cm
・イラストレーターCS4以下でご制作いただきフォントはアウトライン化を施してください。
PDFも一緒に添付していただきますようお願いいたします

■目的
FPによる保険相談のお申込み

■ターゲット
教師・先生

■スケジュール
提案締切:10/12(土)
入稿:10/18(金)
構成案は添付ファイル参照
※キャッチ変え4パターンですが、提案は1パターンでOKです。
ご担当が確定次第、残3パターンを展開いただく予定です。
暖色系
• 高解像度JPG (.jpg)
• イラストレーター形式 (.ai)
専門新聞1面での出稿ですが、スペースが小さいので、とにかく目立たせたいです。
本屋のPOPのような強いビジュアルをイメージしております。
ロゴ素材を添付いたします。

小スペースでのインパクトが最も強かったため

このたびは、多数のご提案ありがとうございました。
残念ながら、採用できなかった方も良い案で迷いました。

引続き、依頼させていただくことがあろうかと思いますが、
今後ともよろしくお願いいたします。

```html
<!DOCTYPE html>
<html lang="ja">
<head>
<meta charset="utf-8">
<title>保険えらびかた相談 広告</title>
<link href="https://fonts.googleapis.com/css2?family=M+PLUS+1p:wght@500;800;900&family=Dela+Gothic+One&display=swap" rel="stylesheet">
<style>
  :root{
    --magenta:#e4007f;
    --yellow:#fff100;
    --ink:#1a1a1a;
    --white:#ffffff;
  }
  *{margin:0;padding:0;box-sizing:border-box;}
  html,body{width:771px;height:1200px;overflow:hidden;background:var(--white);}
  body{font-family:"M PLUS 1p",sans-serif;color:var(--ink);}
  .ad{position:relative;width:771px;height:1200px;border:5px solid var(--magenta);overflow:hidden;}

  /* headline area */
  .headline{position:absolute;left:0;top:0;width:761px;height:636px;}
  .catch-bg{position:absolute;left:0;top:0;width:761px;height:636px;}
  .service-strip{position:absolute;left:14px;top:14px;width:86px;height:610px;}
  .free-badge{width:62px;height:62px;background:var(--magenta);color:var(--white);
    font-weight:900;font-size:22px;line-height:1.05;display:flex;flex-direction:column;
    align-items:center;justify-content:center;border-radius:5px;margin-left:12px;}
  .service-name{writing-mode:vertical-rl;text-orientation:upright;font-weight:900;
    color:var(--magenta);font-size:56px;line-height:1;letter-spacing:4px;margin:14px auto 0;}
  .lead{position:absolute;left:112px;top:16px;width:250px;height:600px;
    writing-mode:vertical-rl;font-weight:800;font-size:33px;line-height:48px;letter-spacing:1px;white-space:nowrap;}
  .catch-question{position:absolute;right:6px;top:8px;writing-mode:vertical-rl;text-orientation:upright;
    font-family:"Dela Gothic One",sans-serif;color:var(--white);font-size:116px;line-height:1;
    white-space:nowrap;}
  .catch-main{position:absolute;left:428px;top:60px;writing-mode:vertical-rl;text-orientation:upright;
    font-family:"Dela Gothic One",sans-serif;color:var(--yellow);font-size:180px;line-height:1;
    white-space:nowrap;text-shadow:5px 5px 0 rgba(0,0,0,.22);}

  /* offer band */
  .offer{position:absolute;left:0;top:636px;width:761px;height:232px;background:var(--yellow);}
  .offer-inner{position:absolute;left:0;top:14px;width:640px;text-align:center;}
  .offer-lead{font-weight:900;font-size:38px;line-height:1.2;}
  .offer-lead .accent{color:var(--magenta);}
  .offer-row{display:flex;align-items:center;justify-content:center;gap:12px;margin-top:4px;white-space:nowrap;}
  .voucher-tag{background:var(--magenta);color:var(--white);font-weight:900;font-size:24px;
    line-height:1.05;padding:6px 8px;border-radius:4px;}
  .voucher-amount{font-family:"Dela Gothic One",sans-serif;color:var(--magenta);font-size:80px;line-height:1.05;}
  .voucher-note{font-weight:900;font-size:36px;line-height:1.2;margin-top:2px;}

  /* terms */
  .terms{position:absolute;left:14px;top:880px;width:733px;display:grid;
    grid-template-columns:1fr 1fr;column-gap:18px;font-weight:500;font-size:17px;line-height:1.38;}

  /* contact */
  .contact-bar{position:absolute;left:0;top:1044px;width:761px;height:40px;background:var(--magenta);
    color:var(--white);display:flex;align-items:center;justify-content:space-between;padding:0 14px;
    font-weight:800;font-size:22px;white-space:nowrap;}
  .contact-bar .hours{font-size:19px;}
  .tel{position:absolute;left:10px;top:1086px;font-family:"Dela Gothic One",sans-serif;
    color:var(--magenta);font-size:56px;line-height:1.05;white-space:nowrap;}

  .footer{position:absolute;left:0;top:1148px;width:761px;height:42px;display:flex;
    align-items:center;justify-content:space-between;padding:0 12px;border-top:2px solid var(--magenta);}
  .brand{display:flex;align-items:center;gap:10px;font-weight:800;font-size:28px;line-height:1;color:var(--magenta);}
  .brand-dot{width:20px;height:20px;border-radius:50%;background:var(--magenta);}
  .search{display:flex;flex-direction:column;align-items:flex-end;}
  .search-box{display:flex;align-items:center;gap:6px;border:2px solid var(--ink);padding:0 10px;
    font-size:15px;line-height:1.3;font-weight:800;}
  .url{font-size:12px;line-height:1.2;font-weight:500;}
</style>
</head>
<body>
<div class="ad">
  <section class="headline">
    <svg class="catch-bg" viewBox="0 0 761 636" aria-hidden="true">
      <polygon points="470,0 761,0 761,636 370,636 370,300" fill="#e4007f"/>
    </svg>
    <div class="service-strip">
      <div class="free-badge"><span>出張</span><span>無料</span></div>
      <div class="service-name">保険えらびかた相談</div>
    </div>
    <p class="lead">増税、年金不安、出費は減らず…。<br>センセイだって、家計が心配な今日<br>この頃。そこで保険相談。保険料を<br>節約し、保険でおカネを貯める方法、<br>プロが教えます。</p>
    <div class="catch-main">家計！</div>
    <div class="catch-question">どうする？</div>
  </section>

  <section class="offer">
    <div class="offer-inner">
      <p class="offer-lead">今なら、<br><span class="accent">ご相談された方全員に</span></p>
      <div class="offer-row">
        <span class="voucher-tag">商品<br>券</span>
        <span class="voucher-amount">5,000円</span>
      </div>
      <p class="voucher-note">プレゼント！</p>
    </div>
  </section>

  <section class="terms">
    <div>
      <p>●サービス対象年齢20〜70歳</p>
      <p>●受付時に登録した個人情報は、サービス提供、商品券発送時に利用します。</p>
    </div>
    <div>
      <p>●商品券は、相談後2ヶ月をめどに、株式会社えらびばより発送されます。</p>
      <p>●職業、健康状態、申告内容、相談に必要な情報提供の可否により、サービスを提供できない場合があります。※詳細はホームページ利用規約をご参照ください。</p>
    </div>
  </section>

  <div class="contact-bar">
    <span>お気軽にお問合せください。</span>
    <span class="hours">受付：9:00〜18:00（土日祝休）</span>
  </div>
  <div class="tel">TEL:0120-000-123</div>

  <footer class="footer">
    <div class="brand"><span class="brand-dot"></span><span>保険のえらびば</span></div>
    <div class="search">
      <div class="search-box">
        <svg width="15" height="15" viewBox="0 0 18 18" aria-hidden="true"><circle cx="7" cy="7" r="5" fill="none" stroke="#1a1a1a" stroke-width="2"/><line x1="11" y1="11" x2="16" y2="16" stroke="#1a1a1a" stroke-width="2.5"/></svg>
        <span>保険のえらびば</span>
      </div>
      <span class="url">www.hoken-erabiba.example</span>
    </div>
  </footer>
</div>
</body>
</html>
```